Natural healthcare clinic needs stationery and business card design

We have had a logo developed by Pixel Harbor and are now looking at utilising it for a new business concept. The concept is a natural healthcare clinic that hosts a number of small businesses. The individual practitioners may want to utilise the host business stationery to provide a consistent message to clients.

I am looking for a stationery design - letterhead, DL brochure template and business card that uses our logo. The business name 'Verdant Tides' is all about getting rhythm back into your life so you can be fit and healthy. The stationery design should reflect this.

There are a couple of requirements for the business card, it needs to be double-sided with black and white back. There should be lines to write appointment times on. The cards may need to be custom named on the front for example Marcia Tolk, Remedial Therapist and Aromatherapist. Therefore if a template can be provided so we can customise this information using MS Publisher, it would be appreciated.

The DL brochure template needs to be A4 folded to DL. I am looking for a consistent brand message that can be utilised to produce our own clinic brochures.

The natural healthcare clinic will host the following types of businesses - remedial massage, pregnancy massage, oncology massage, aromatherapy, acupuncture - as a bit of a guide.

Target Market(s)

25-45 year old male and females who work full time.

Industry/Entity Type

Healthcare

Requirements
Must have
• Use the logo I have already.

```html
<!DOCTYPE html>
<html lang="en">
<head>
<meta charset="utf-8">
<title>Verdant Tides – Business Card</title>
<link href="https://fonts.googleapis.com/css2?family=Open+Sans:wght@300;400;600&display=swap" rel="stylesheet">
<style>
  :root {
    --page: #e9e6df;
    --card-white: #ffffff;
    --olive-deep: #2c3208;
    --olive: #4f6a12;
    --olive-bright: #6f8f1c;
    --lime: #9cc43a;
    --peach: #f5c7a1;
    --ink-olive: #5a6420;
    --ink-grey: #555a48;
    --icon-orange: #e9772a;
    --text-light: #f3f4ea;
  }
  * { margin: 0; padding: 0; box-sizing: border-box; }
  html, body {
    width: 1200px; height: 1024px; overflow: hidden;
    background: var(--page);
    font-family: "Open Sans", Arial, sans-serif;
  }
  .sheet {
    width: 1200px; height: 1024px;
    display: flex; flex-direction: column; align-items: center; justify-content: center;
    gap: 40px;
  }
  .card {
    position: relative;
    width: 780px; height: 446px;
    border-radius: 28px;
    overflow: hidden;
    box-shadow: 0 10px 26px rgba(40, 40, 20, 0.22);
  }
  /* ---------- front ---------- */
  .card-front { background: var(--card-white); }
  .front-band { position: absolute; inset: 0; width: 100%; height: 100%; }
  .brand-block {
    position: absolute; left: 60px; top: 196px;
    display: flex; align-items: center; gap: 14px;
  }
  .brand-dot {
    width: 28px; height: 28px; border-radius: 50%;
    background: var(--lime); flex: none;
  }
  .brand-name {
    font-size: 48px; font-weight: 300; color: var(--ink-olive);
    letter-spacing: -0.5px; white-space: nowrap; line-height: 1.1;
  }
  .divider {
    position: absolute; left: 450px; top: 274px; width: 180px; height: 2px;
    background: linear-gradient(90deg, rgba(111,143,28,0), var(--olive-bright) 40%, rgba(111,143,28,0));
  }
  .contact {
    position: absolute; left: 440px; top: 36px; width: 250px;
    color: var(--ink-grey);
  }
  .contact-name {
    font-size: 18px; font-weight: 400; color: var(--ink-olive);
    margin-bottom: 16px; white-space: nowrap;
  }
  .contact-name .role { color: var(--lime); }
  .contact-address { font-size: 13.5px; line-height: 1.45; margin-bottom: 12px; }
  .contact-list { list-style: none; font-size: 13.5px; line-height: 1.7; }
  .contact-list li { display: flex; align-items: center; gap: 8px; }
  .contact-list svg { width: 12px; height: 12px; flex: none; }
  .front-web {
    position: absolute; left: 48px; bottom: 28px;
    font-size: 15px; color: var(--text-light); letter-spacing: 0.3px;
  }
  /* ---------- back ---------- */
  .card-back {
    background: radial-gradient(ellipse at 55% 45%, var(--olive-bright) 0%, var(--olive) 45%, var(--olive-deep) 100%);
  }
  .back-brand {
    position: absolute; left: 50%; top: 50%;
    transform: translate(-50%, -70%);
    display: flex; align-items: center; gap: 16px;
  }
  .back-brand .brand-name { color: var(--text-light); font-size: 54px; }
  .back-brand .brand-dot { background: var(--peach); }
  .back-web {
    position: absolute; left: 0; right: 0; top: 262px;
    text-align: center; font-size: 16px; color: var(--text-light); letter-spacing: 0.4px;
  }
</style>
</head>
<body>
<main class="sheet">

  <section class="card card-front" aria-label="Business card front">
    <svg class="front-band" viewBox="0 0 780 446" preserveAspectRatio="none" aria-hidden="true">
      <path d="M0 318 C 250 388, 560 368, 690 258 C 750 198, 765 98, 780 28 L780 446 L0 446 Z" fill="var(--lime)"/>
      <path d="M0 324 C 250 394, 560 374, 690 264 C 750 204, 765 104, 780 34 L780 446 L0 446 Z" fill="var(--card-white)"/>
      <path d="M0 332 C 250 402, 560 382, 690 272 C 750 212, 765 112, 780 42 L780 446 L0 446 Z" fill="var(--peach)"/>
      <path d="M0 344 C 250 414, 560 394, 696 284 C 754 224, 768 124, 780 56 L780 446 L0 446 Z" fill="var(--olive)"/>
      <path d="M0 352 C 250 424, 566 404, 704 294 C 758 236, 770 140, 780 74 L780 446 L0 446 Z" fill="var(--olive-deep)"/>
    </svg>

    <div class="brand-block">
      <span class="brand-dot"></span>
      <span class="brand-name">Verdant Tides</span>
    </div>

    <div class="divider"></div>

    <div class="contact">
      <p class="contact-name">Arlen Voss <span class="role">| Job Title</span></p>
      <p class="contact-address">Your address Goes Here, City,<br>Zip Code, Country Name</p>
      <ul class="contact-list">
        <li><svg viewBox="0 0 12 12"><path d="M3 1 L5 3 L4 5 Q5 7 7 8 L9 7 L11 9 L9 11 Q2 10 1 3 Z" fill="var(--icon-orange)"/></svg>415-2290-7731</li>
        <li><svg viewBox="0 0 12 12"><rect x="1" y="3" width="10" height="7" rx="1" fill="var(--icon-orange)"/><rect x="3" y="1" width="6" height="3" fill="var(--icon-orange)"/></svg>415-6603-1184</li>
        <li><svg viewBox="0 0 12 12"><rect x="1" y="2.5" width="10" height="7" fill="var(--icon-orange)"/><path d="M1 2.5 L6 7 L11 2.5" fill="none" stroke="#fff" stroke-width="1"/></svg>hello@verdanttides.com</li>
      </ul>
    </div>

    <p class="front-web">www.verdanttides.com</p>
  </section>

  <section class="card card-back" aria-label="Business card back">
    <div class="back-brand">
      <span class="brand-dot"></span>
      <span class="brand-name">Verdant Tides</span>
    </div>
    <p class="back-web">www.verdanttides.com</p>
  </section>

</main>
</body>
</html>
```